Unique and original Business Card for Financial Services Business

I have moved premises and need to change the detail on my business card so thought now is a good time for a re-design. Looking for something professional and modern with colours to fit in with out logo. Like the idea of foil or embossing if that works but not a must have but I do want something that stands out and that I could not design myself.

Once business card is designed I will also be looking to get letterhead and flyers done but want the business card concept in place first.

The majority of designs I am receiving are generic and template based. I am looking for something unique and original. We have some great design elements in our logo, think outside the box and show me something that stands out from the crowd.

Target Market(s)

Business Professionals

Industry/Entity Type

Finance

Contact Information for Business Card

Name: Delia Norwood Phone 0473 958 162 Address PO Box 8617 Mossvale NSW 2389 Email info@steadyharbourfinancialservices.com.au website www.steadyharbourfinancialservices.com.au

Font styles to use
Other font styles liked:
• Ralway

Requirements
Should not have
• No black backgrounds please

```html
<!DOCTYPE html>
<html lang="en">
<head>
<meta charset="utf-8">
<title>Steady Harbour Financial Services — Business Card</title>
<link rel="stylesheet" href="https://fonts.googleapis.com/css2?family=Montserrat:wght@700&family=Poppins:wght@400&family=Raleway:wght@300&display=swap">
<style>
  :root {
    --bg: #d9dadb;
    --paper: #ffffff;
    --teal: #0e7c86;
    --teal-deep: #065a72;
    --teal-light: #119690;
    --ink: #3a3d40;
    --muted-silver: #c9ccd0;
  }
  * { box-sizing: border-box; margin: 0; padding: 0; }
  html, body { width: 1200px; height: 800px; overflow: hidden; }
  body {
    background: var(--bg);
    display: flex;
    align-items: center;
    justify-content: center;
    gap: 40px;
    font-family: "Poppins", sans-serif;
  }
  .card {
    position: relative;
    width: 540px;
    height: 324px;
    border-radius: 22px;
    overflow: hidden;
    box-shadow: 0 10px 24px rgba(0,0,0,0.18);
  }

  /* Front side */
  .card--front { background: var(--paper); }
  .card__ornament {
    position: absolute;
    left: 0; top: 0;
    width: 230px; height: 324px;
  }
  .card__details {
    position: absolute;
    right: 30px; top: 32px;
    width: 300px;
    text-align: right;
  }
  .brand {
    display: flex;
    align-items: center;
    justify-content: flex-end;
    gap: 10px;
    font-family: "Raleway", sans-serif;
    font-weight: 300;
    color: var(--teal);
  }
  .brand__mark {
    width: 30px; height: 30px;
    border-radius: 50%;
    background: var(--teal);
    flex: none;
  }
  .brand__name { line-height: 1.1; }
  .brand__name span { display: block; }
  .brand__title { font-size: 19px; letter-spacing: 0.5px; }
  .brand__sub { font-size: 11px; letter-spacing: 4px; }

  .person {
    margin-top: 26px;
    font-family: "Montserrat", sans-serif;
    font-weight: 700;
    font-size: 22px;
    color: var(--teal);
  }
  .address {
    margin-top: 6px;
    font-size: 11px;
    line-height: 1.5;
    color: var(--ink);
  }
  .contact {
    list-style: none;
    margin-top: 22px;
    font-size: 11px;
    line-height: 1.9;
    color: var(--ink);
  }
  .contact li {
    display: flex;
    align-items: center;
    justify-content: flex-end;
    gap: 7px;
    white-space: nowrap;
  }
  .contact svg { width: 11px; height: 11px; flex: none; }

  /* Back side */
  .card--back {
    background: linear-gradient(125deg, var(--teal-deep) 0%, var(--teal) 55%, var(--teal-light) 100%);
    display: flex;
    align-items: center;
    justify-content: center;
  }
  .card--back .brand { color: var(--paper); gap: 14px; }
  .card--back .brand__mark { width: 44px; height: 44px; background: var(--paper); }
  .card--back .brand__title { font-size: 30px; }
  .card--back .brand__sub { font-size: 16px; letter-spacing: 6px; }
</style>
</head>
<body>

  <section class="card card--front" aria-label="Business card front">
    <svg class="card__ornament" viewBox="0 0 230 324" role="img" aria-label="Flowing teal and silver decorative swirl motif">
      <defs>
        <linearGradient id="swirl-tone" x1="0" y1="0" x2="1" y2="1">
          <stop offset="0" stop-color="#0a6f80"/>
          <stop offset="0.6" stop-color="#0e7c86"/>
          <stop offset="1" stop-color="#cfd2d6"/>
        </linearGradient>
      </defs>
      <path d="M0 0 H120 C190 60 235 170 200 324 H0 Z" fill="url(#swirl-tone)"/>
    </svg>

    <div class="card__details">
      <div class="brand">
        <span class="brand__mark"></span>
        <div class="brand__name">
          <span class="brand__title">STEADY HARBOUR</span>
          <span class="brand__sub">Financial Services</span>
        </div>
      </div>

      <p class="person">Delia Norwood</p>
      <p class="address">PO Box 8617 Mossvale<br>NSW 2389</p>

      <ul class="contact">
        <li>0473 958 162
          <svg viewBox="0 0 24 24" aria-hidden="true"><path fill="#0e7c86" d="M6.6 10.8a15 15 0 0 0 6.6 6.6l2.2-2.2c.3-.3.7-.4 1-.2 1.1.4 2.3.6 3.6.6.6 0 1 .4 1 1V20c0 .6-.4 1-1 1A17 17 0 0 1 3 4c0-.6.4-1 1-1h3.5c.6 0 1 .4 1 1 0 1.3.2 2.5.6 3.6.1.3 0 .7-.2 1z"/></svg>
        </li>
        <li>info@steadyharbourfinancialservices.com.au
          <svg viewBox="0 0 24 24" aria-hidden="true"><rect x="2" y="5" width="20" height="14" rx="2" fill="#0e7c86"/><path d="M3 6l9 7 9-7" stroke="#fff" stroke-width="1.8" fill="none"/></svg>
        </li>
        <li>www.steadyharbourfinancialservices.com.au
          <svg viewBox="0 0 24 24" aria-hidden="true"><circle cx="12" cy="12" r="10" fill="#0e7c86"/><path d="M2 12h20M12 2c3 3 3 17 0 20M12 2c-3 3-3 17 0 20" stroke="#fff" stroke-width="1.5" fill="none"/></svg>
        </li>
      </ul>
    </div>
  </section>

  <section class="card card--back" aria-label="Business card back">
    <div class="brand">
      <span class="brand__mark"></span>
      <div class="brand__name">
        <span class="brand__title">STEADY HARBOUR</span>
        <span class="brand__sub">Financial Services</span>
      </div>
    </div>
  </section>

</body>
</html>
```